5 Planner Covers for Teacher Planners

Hello,
I currently run a Speech-Language Pathologist website and have created a planner for my fellow Speech Therapist. I would like someone to create 5 different planner covers so my followers will have different options to choose from.
Here is my planner from last year to give you an idea of what the planner will look like http://www.talkbloomshop.example/free-slp-planner/
My followers are mostly women aged 25-50. However, I don't want the covers to be overly girly or excessive with flowers. Simple is better.
I'd also like there to be an editable text box to allow the Speech Therapist to type their name on their cover if they wish.
Planner Cover can say any of the following: SLP Planner, Planner, Speech Therapy Planner, Speech-Language Pathologist (maybe this title could be editable as well??).
To give you an idea I have uploaded a screenshot of last year's planners cover that I made myself.
What I am looking for:
-Size 8.5" by 11"
-5 different planner covers
-1 gender-neutral cover
-simple design
-limited flowers (or overly girly
-text box to add a personal name
-Possible titles: SLP Planner, Planner, Speech Therapy Planner, Speech-Language Pathologist (maybe this title could be editable as well??)
Target Market(s)
Women aged 25-50
Colors
Designer to choose colors to be used in the design.
Requirements
Must have
- What I am looking for:
-Size 8.5" by 11"
-1 gender-neutral cover
-simple design
Nice to have
- I've uploaded some that I like from Craftora to give you an idea.
Here is my craftora store https://www.craftora.example/shop/QuietMeadowHome to give you an idea of things I like.
I like Marla Pendry and her simple elegant rustic style.

```html
<!DOCTYPE html>
<html lang="en">
<head>
<meta charset="utf-8">
<title>Speech Therapy Planner Cover</title>
<link rel="stylesheet" href="https://fonts.googleapis.com/css2?family=Open+Sans:wght@300;700;800&display=swap">
<style>
  :root {
    --cream: #fdf9f4;
    --blush: #f4c3b4;
    --sage: #dfe6c4;
    --mist: #cfe0dd;
    --cobalt: #0c55a3;
    --white: #ffffff;
  }
  html, body {
    margin: 0;
    padding: 0;
    overflow: hidden;
  }
  .cover {
    position: relative;
    width: 927px;
    height: 1200px;
    overflow: hidden;
    background: var(--cream);
    font-family: "Open Sans", Arial, sans-serif;
  }
  .cover__pattern {
    position: absolute;
    inset: 0;
    background:
      radial-gradient(circle at 12% 18%, rgba(244,195,180,0.45), transparent 22%),
      radial-gradient(circle at 88% 10%, rgba(207,224,221,0.55), transparent 24%),
      radial-gradient(circle at 80% 78%, rgba(244,195,180,0.40), transparent 26%),
      radial-gradient(circle at 15% 85%, rgba(207,224,221,0.50), transparent 25%),
      radial-gradient(circle at 50% 50%, rgba(223,230,196,0.35), transparent 60%),
      var(--cream);
  }
  .title-panel {
    position: absolute;
    left: 220px;
    top: 365px;
    width: 533px;
    height: 468px;
    background: var(--cobalt);
    color: var(--white);
  }
  .title-panel__line {
    position: absolute;
    left: 41px;
    margin: 0;
    line-height: 1;
    white-space: nowrap;
  }
  .title-panel__line--strong {
    font-weight: 800;
    font-size: 104px;
    letter-spacing: -2px;
  }
  .title-panel__line--speech { top: 90px; }
  .title-panel__line--therapy { top: 181px; }
  .title-panel__line--light {
    top: 275px;
    font-weight: 300;
    font-size: 104px;
    letter-spacing: -1px;
  }
</style>
</head>
<body>
  <main class="cover">
    <div class="cover__pattern" role="img" aria-label="Soft repeating pattern of pastel flowers, hearts and leafy vines on a cream background"></div>
    <section class="title-panel">
      <h1 class="title-panel__line title-panel__line--strong title-panel__line--speech">SPEECH</h1>
      <p class="title-panel__line title-panel__line--strong title-panel__line--therapy">THERAPY</p>
      <p class="title-panel__line title-panel__line--light">PLANNER</p>
    </section>
  </main>
</body>
</html>
```